TotPlanet Community Landing Page

TotPlanet is a virtual world built with childrens' needs in mind. It is an online portal where parents will find all kids' related stuffs and a community connect point for parents to interact and share their experiences.

We need the designs for 2 pages within TotPlanet:
- Landing Page for the Community Area
- Registration page for membership

1) The Landing Page need to have the following:

Logo & Main Background :- use the images attached

Page Title & Navigation Menu :-
The page title is "Community Connect"; navigation menu should be able to hold at least 6 tabs

Login Widget* :-
We want to put emphasis on the design of this.
For visitors, this is a normal login widget with username/password input fields, register button and 'login with chatterbook' button.
For logged-in users, this becomes a simple dashboard widget with Avatar, shortlinks and some useful navigation buttons.

"Groups" Section :-
This area holds an image, a short paragraph introducing "Groups", a widget showing 5-10 latest/popular groups and a 'Go to Groups' button at the bottom.

"Forum" Section :-
This area holds an image, a short paragraph introducing "Forum", a widget showing 5-10 latest/popular discussion topics and a 'Go to Forum' button at the bottom.

"Activities" Section -
This area holds an image, a short paragraph introducing "Forum", a widget showing 5-10 latest/popular events & activities and a 'Go to Activities' button at the bottom.

"Marketplace" Section :-
This area holds an image, a short paragraph introducing "Marketplace", a widget showing 5-10 latest/popular products and a 'Go to Marketplace' button at the bottom.

Social Media elements :-
The usual social media icons and chatterbook like box.

2) The Registration Page will need to contain the registration form as per the image attached.

Target Market(s)

Parents with kids ranging from 2 - 12 years old

Industry/Entity Type

Events

Requirements
Nice to have
• - colorful illustrations of kids or kids related images all around

```html
<!DOCTYPE html>
<html lang="en">
<head>
<meta charset="utf-8">
<title>TotPlanet – Community Connect</title>
<link href="https://fonts.googleapis.com/css2?family=Arimo:ital,wght@0,400;0,700;1,400&display=swap" rel="stylesheet">
<style>
:root{
  --sky-top:#bfe9f4;
  --sky-mid:#33b3e2;
  --grass:#5e8f1e;
  --grass-light:#9cc43a;
  --nav-green:#a8d24a;
  --nav-border:#86b32c;
  --panel:#ffffff;
  --ink:#333333;
  --body:#555555;
  --muted:#999999;
  --rule:#d4d4d4;
  --groups:#e8722a;
  --forum:#7a9a22;
  --activities:#b530d8;
  --market:#a83c3c;
  --brand:#d8197c;
  --login:#b446d6;
  --home:#d0101a;
  --marketplace-tab:#f47a1c;
  --activities-tab:#a84040;
  --groups-tab:#a820c8;
  --forums-tab:#34a8da;
  --contact-tab:#5cb82a;
  --social:#3f6fb4;
}
*{margin:0;padding:0;box-sizing:border-box}
html,body{width:1200px;height:1000px;overflow:hidden}
body{font-family:"Arimo",Arial,sans-serif;position:relative;background:var(--sky-mid)}
.scenery{position:absolute;inset:0;
  background:linear-gradient(180deg,var(--sky-top) 0%,#7fd0ec 18%,var(--sky-mid) 40%,#9fd6ea 52%,var(--grass-light) 62%,var(--grass) 80%,#4c7a16 100%)}
.brand{position:absolute;left:165px;top:52px;display:flex;align-items:center;gap:10px;z-index:3}
.brand-dot{width:34px;height:34px;border-radius:50%;background:var(--brand)}
.brand-name{font-size:40px;font-weight:700;color:var(--brand)}
.social{position:absolute;top:30px;left:825px;display:flex;gap:6px}
.social span{width:32px;height:32px;border-radius:50%;background:var(--social)}
.social span:nth-child(2){background:#4fb4ea}
.social span:nth-child(3){background:#3a8cc4}
.login-btn{position:absolute;left:950px;top:30px;width:93px;height:32px;border-radius:5px;background:var(--login);border:2px solid #d486ee;color:#fff;font-weight:700;font-size:15px;display:flex;align-items:center;justify-content:center;gap:8px}
.login-btn svg{width:18px;height:18px}
.nav{position:absolute;left:153px;top:81px;width:900px;height:66px;background:var(--nav-green);border:2px solid var(--nav-border);border-radius:8px;z-index:2}
.nav-tab{position:absolute;top:16px;height:32px;border-radius:16px;color:#fff;font-weight:700;font-size:15px;display:flex;align-items:center;justify-content:center;box-shadow:inset 0 -2px 0 rgba(0,0,0,.15)}
.panel{position:absolute;left:172px;top:172px;width:863px;height:900px;background:var(--panel);border-radius:40px}
.page-title{position:absolute;left:198px;top:205px;font-size:28px;font-weight:700;color:var(--ink)}
.hrule{position:absolute;left:200px;width:812px;border-top:1px dashed var(--rule)}
.vrule{position:absolute;left:594px;border-left:1px dashed var(--rule)}
.section{position:absolute;width:370px}
.section-head{display:flex;align-items:center;gap:8px;font-size:22px;font-weight:700;padding:0 0 8px 6px;border-bottom:1px solid var(--rule);width:356px}
.section-head svg{width:26px;height:24px}
.item{position:relative;height:89px;margin-top:0}
.thumb{position:absolute;left:0;top:0;width:74px;height:74px;border:3px solid #fff;outline:1px solid #ddd;box-shadow:0 1px 3px rgba(0,0,0,.15)}
.item-title{position:absolute;left:87px;top:-2px;font-size:15px;font-weight:700;white-space:nowrap}
.item-date{position:absolute;left:88px;top:18px;font-size:11px;font-style:italic;font-weight:700;color:var(--muted)}
.item-text{position:absolute;left:88px;top:37px;width:240px;font-size:11.5px;line-height:17px;font-weight:700;color:var(--body)}
.groups .item-title{color:var(--groups)} .forum .item-title{color:var(--forum)}
.activities .item-title{color:var(--activities)} .market .item-title{color:var(--market)}
.items{margin-top:18px}
.go-btn{position:absolute;height:30px;border-radius:4px;color:#fff;font-weight:700;font-size:15px;display:flex;align-items:center;justify-content:center;border:2px solid rgba(255,255,255,.6);box-shadow:0 0 0 1px rgba(0,0,0,.12)}
</style>
</head>
<body>
<div class="scenery" role="img" aria-label="Cartoon sky with sun rays, rainbow, clouds and green hills with leafy bushes"></div>

<div class="brand"><span class="brand-dot"></span><span class="brand-name">TotPlanet</span></div>

<div class="social" aria-label="Social links"><span title="chatterbook"></span><span></span><span></span></div>
<div class="login-btn"><svg viewBox="0 0 18 18"><circle cx="9" cy="9" r="9" fill="#d992f0"/><rect x="5" y="8" width="8" height="6" rx="1" fill="#fff"/><path d="M6.5 8V6.5a2.5 2.5 0 0 1 5 0V8" stroke="#fff" stroke-width="1.5" fill="none"/></svg>Login</div>

<nav class="nav">
  <span class="nav-tab" style="left:270px;width:71px;background:var(--home)">Home</span>
  <span class="nav-tab" style="left:354px;width:122px;background:var(--marketplace-tab)">Marketplace</span>
  <span class="nav-tab" style="left:490px;width:97px;background:var(--activities-tab)">Activities</span>
  <span class="nav-tab" style="left:600px;width:83px;background:var(--groups-tab)">Groups</span>
  <span class="nav-tab" style="left:696px;width:84px;background:var(--forums-tab)">Forums</span>
  <span class="nav-tab" style="left:793px;width:89px;background:var(--contact-tab)">Contact</span>
</nav>

<div class="panel"></div>
<h1 class="page-title">Community Connect :</h1>
<div class="hrule" style="top:250px"></div>
<div class="vrule" style="top:262px;height:615px"></div>
<div class="hrule" style="top:889px"></div>
<div class="vrule" style="top:904px;height:100px"></div>

<section class="section groups" style="left:205px;top:260px">
  <h2 class="section-head" style="color:var(--groups)"><svg viewBox="0 0 26 24"><circle cx="9" cy="7" r="5" fill="currentColor"/><circle cx="18" cy="8" r="4" fill="currentColor"/><path d="M0 22a9 8 0 0 1 18 0z M14 22a8 7 0 0 1 12 0z" fill="currentColor"/></svg>Groups</h2>
  <div class="items" style="margin-left:-2px">
    <div class="item"><div class="thumb" role="img" aria-label="Photo of kids playing" style="background:linear-gradient(135deg,#d9b89a,#8a6a50)"></div><div class="item-title" style="left:87px">Lorem Ipsum</div><div class="item-date">Tue, July 16, 2013</div><p class="item-text">Lorem Ipsum is simply dummy text of the printing and typesetting industry...</p></div>
    <div class="item"><div class="thumb" role="img" aria-label="Photo of smiling children" style="background:linear-gradient(135deg,#e8c8a8,#a07050)"></div><div class="item-title">Many variations</div><div class="item-date">Sun, July 10, 2013</div><p class="item-text">Lorem Ipsum is simply dummy text of the printing and typesetting industry...</p></div>
    <div class="item"><div class="thumb" role="img" aria-label="Photo of kids reading together" style="background:linear-gradient(135deg,#c8b0a0,#5070a0)"></div><div class="item-title" style="left:84px">Nowe szaty PixNews...</div><div class="item-date">Mon, July 04, 2013</div><p class="item-text">Lorem Ipsum is simply dummy text of the printing and typesetting industry...</p></div>
    <div class="item"><div class="thumb" role="img" aria-label="Photo of group of children" style="background:linear-gradient(135deg,#cfe3b0,#e0a0a0)"></div><div class="item-title" style="left:84px">nowe avatarki (Parkside)/QDS/</div><div class="item-date">Wed, June 21, 2013</div><p class="item-text">Lorem Ipsum is simply dummy text of the printing and typesetting industry...</p></div>
    <div class="item"><div class="thumb" role="img" aria-label="Photo of kids standing in a row" style="background:linear-gradient(135deg,#f0e0c0,#c08060)"></div><div class="item-title" style="left:84px">wyglad (Uwagi / Propozycje)...</div><div class="item-date">Thu, June 15, 2013</div><p class="item-text">Lorem Ipsum is simply dummy text of the printing and typesetting industry...</p></div>
    <div class="item"><div class="thumb" role="img" aria-label="Photo of two children lying down" style="background:linear-gradient(135deg,#e8d0c0,#d04040)"></div><div class="item-title" style="left:84px">Rozbieranie orchard pro...</div><div class="item-date">Fri, June 11, 2013</div><p class="item-text">Lorem Ipsum is simply dummy text of the printing and typesetting industry...</p></div>
  </div>
</section>
<div class="go-btn" style="left:429px;top:846px;width:124px;background:var(--groups)">Go to Groups</div>

<section class="section forum" style="left:626px;top:260px">
  <h2 class="section-head" style="color:var(--forum)"><svg viewBox="0 0 26 24"><ellipse cx="10" cy="10" rx="10" ry="7" fill="currentColor"/><path d="M4 15l-2 5 6-3z" fill="currentColor"/><ellipse cx="18" cy="14" rx="8" ry="6" fill="currentColor" opacity=".75"/></svg>Forum</h2>
  <div class="items">
    <div class="item"><div class="thumb" role="img" aria-label="Photo of a smiling girl" style="background:linear-gradient(135deg,#e8b090,#c03030)"></div><div class="item-title">Deconstructing Sola Scriptura...</div><div class="item-date">Tue, July 16, 2013</div><p class="item-text">Lorem Ipsum is simply dummy text of the printing and typesetting industry...</p></div>
    <div class="item"><div class="thumb" role="img" aria-label="Photo of a boy painting" style="background:linear-gradient(135deg,#f0d040,#c07050)"></div><div class="item-title">Widget gadget4day (software)...</div><div class="item-date">Sun, July 10, 2013</div><p class="item-text">Lorem Ipsum is simply dummy text of the printing and typesetting industry...</p></div>
    <div class="item"><div class="thumb" role="img" aria-label="Photo of a little girl" style="background:linear-gradient(135deg,#d8a080,#702020)"></div><div class="item-title">Nowe szaty PixNews...</div><div class="item-date">Mon, July 04, 2013</div><p class="item-text">Lorem Ipsum is simply dummy text of the printing and typesetting industry...</p></div>
    <div class="item"><div class="thumb" role="img" aria-label="Photo of a child playing with blocks" style="background:linear-gradient(135deg,#f0e0d0,#c08860)"></div><div class="item-title">nowe avatarki (Parkside)/QDS/</div><div class="item-date">Wed, June 21, 2013</div><p class="item-text">Lorem Ipsum is simply dummy text of the printing and typesetting industry...</p></div>
    <div class="item"><div class="thumb" role="img" aria-label="Photo of a parent with a child" style="background:linear-gradient(135deg,#c8e0a0,#e0c0a0)"></div><div class="item-title">wyglad (Uwagi / Propozycje)...</div><div class="item-date">Thu, June 15, 2013</div><p class="item-text">Lorem Ipsum is simply dummy text of the printing and typesetting industry...</p></div>
    <div class="item"><div class="thumb" role="img" aria-label="Photo of a mother and child" style="background:linear-gradient(135deg,#f4e8e0,#b06050)"></div><div class="item-title">Rozbieranie orchard pro...</div><div class="item-date">Fri, June 11, 2013</div><p class="item-text">Lorem Ipsum is simply dummy text of the printing and typesetting industry...</p></div>
  </div>
</section>
<div class="go-btn" style="left:850px;top:846px;width:120px;background:var(--contact-tab)">Go to Forum</div>

<section class="section activities" style="left:205px;top:900px">
  <h2 class="section-head" style="color:var(--activities)"><svg viewBox="0 0 26 24"><path d="M11 2a10 9 0 1 0 0 19c2 0 2-2 1-3s0-3 2-3h3a4 4 0 0 0 4-5C20 5 16 2 11 2z" fill="currentColor"/><circle cx="6" cy="10" r="2" fill="#fff"/><circle cx="10" cy="6" r="2" fill="#fff"/><path d="M19 22l6-16" stroke="currentColor" stroke-width="2.5"/></svg>Activities</h2>
  <div class="items" style="margin-top:18px">
    <div class="item"><div class="thumb" role="img" aria-label="Photo of children doing an activity" style="background:linear-gradient(135deg,#e8c8b0,#b05030)"></div><div class="item-title">Lorem Ipsum</div><div class="item-date">Tue, July 16, 2013</div><p class="item-text">Lorem Ipsum is simply dummy text of the printing and typesetting industry...</p></div>
  </div>
</section>

<section class="section market" style="left:626px;top:900px">
  <h2 class="section-head" style="color:var(--market)"><svg viewBox="0 0 26 24"><circle cx="12" cy="12" r="10" fill="currentColor"/><path d="M6 8c3 0 4 2 3 4s1 4 3 5M15 4c0 3 3 3 5 5" stroke="#fff" stroke-width="2" fill="none"/></svg>Marketplace</h2>
  <div class="items" style="margin-top:20px">
    <div class="item"><div class="thumb" role="img" aria-label="Photo of children with toys" style="background:linear-gradient(135deg,#e8c0a0,#c04040)"></div><div class="item-title">Deconstructing Sola Scriptura...</div><div class="item-date">Tue, July 16, 2013</div><p class="item-text">Lorem Ipsum is simply dummy text of the printing and typesetting industry...</p></div>
  </div>
</section>
</body>
</html>
```